Lindenfall Studio Business cards

Design our business cards and eventually a logo. The company is based in Paris, its activity is the retailing via internet of luxury home furniture (like Vantorelli, Bercasso, fradusi...) Our clients are international andwith a high sense of aesthetics. The design shall communicate wealth and trust with a high quality and aesthetic sense, pure lines Company Name is Lindenfall StudioExplanation of the name: usually people who wants to buy furniture usually go in a showroom. Today they go in showroom to test the furniture and they search for the price on internet, which is a "Lindenfall studio".We will not be a e-commerce site. Our site will be (another project) a presentation site which purpose is to reach qualified prospects. Then everything will be handled by phone, meeting etc.The business card must be professional as we will negotiate with many luxury brands, opportunity to represent them on our site, prices etc.As far as the color are concerned mostly black and whithe or grey. The font of the Lindenfall Studio name shall have some impact.

Target Market(s)

High-end furniture and buyers of luxury goods, international customers, mostly women who handle such projects.
We also deal with professional buyers (hotels as an example) and luxury brands

Contact Information for Business Card

standard format 85x55, lanscape card, square corners will be printed on thick high quality paper (300 or 350g)

Font styles to use
Sans Serif

Colors

Designer to choose colors to be used in the design.

Requirements
Must have
• Must be white, as the paper will be high quality, the paper will enhance the card.
• Name of the brand Lindenfall studio (with specific font which make it very nice looking and catch the attention. similar to Calibri or Calibri
• Name of person (will give you the name later (4 names and position)
• the position of the person
• Mobile phone, e-mail, Physical address 27, rue Caldenois, 75005 Paris, France (courrier only) our web site www.lindenfallstudio-example.fr
• The card must be simple and class
Nice to have
• Font of the address is smaller than the rest,
• Calibri font or similar on recto side with the name of the company which may look similar to the picture inserted in the brief.
• The grey color in the picture inserted is ok for us
Should not have
• Any parallel lines which represent the name of the company
• Any heavy design If you go on internet sites which present the furniture all designs are pure lines and high quality craftsmanship. To have an idea of our targetted client or brand we will be in touch: https://www.casavornetta-example.it/projects/
• Note that the picture added below is what we use, now as mail signature, up to you to have a better design etc.

```html
<!DOCTYPE html>
<html lang="en">
<head>
<meta charset="utf-8">
<title>Lindenfall Studio – Business Card</title>
<link rel="stylesheet" href="https://fonts.googleapis.com/css2?family=Libre+Franklin:wght@400;500;700;800&display=swap">
<style>
  :root {
    --page-bg: #d9dcd7;
    --card-white: #ffffff;
    --frame-grey: #8a8a8a;
    --rule-grey: #9a9a9a;
    --icon-grey: #6b6b6b;
    --text-strong: #1f1f1f;
    --text-soft: #4a4a4a;
  }
  * { box-sizing: border-box; margin: 0; padding: 0; }
  html, body {
    width: 1200px; height: 1200px; overflow: hidden;
    background: var(--page-bg);
    font-family: "Libre Franklin", Arial, sans-serif;
  }
  .card {
    position: absolute; left: 100px; top: 276px;
    width: 1000px; height: 647px;
    padding: 28px;
    background: var(--card-white);
  }
  .card-face {
    position: relative; width: 100%; height: 100%;
    background: var(--card-white);
    border: 3px solid var(--frame-grey);
    color: var(--text-strong);
  }
  .contact-list {
    position: absolute; right: 42px; top: 50px;
    list-style: none; text-align: right;
  }
  .contact-item {
    display: flex; align-items: center; justify-content: flex-end;
    gap: 22px; font-size: 22px; color: var(--text-soft);
    height: 34px; margin-bottom: 6px; letter-spacing: 0.2px;
  }
  .contact-icon { width: 22px; height: 22px; flex: none; }
  .person {
    position: absolute; left: 54px; top: 186px;
  }
  .person-name { font-size: 25px; font-weight: 700; color: var(--text-strong); }
  .person-role { font-size: 21px; font-weight: 400; color: var(--text-soft); margin-top: 4px; }
  .rule {
    position: absolute; left: 0; right: 0; height: 2px;
    background: var(--rule-grey);
  }
  .rule-top { top: 260px; }
  .rule-bottom { top: 378px; }
  .address {
    position: absolute; left: 0; right: 0; top: 314px;
    text-align: center; font-size: 22px; color: var(--text-soft);
  }
  .brand {
    position: absolute; left: 0; right: 0; top: 430px; text-align: center;
  }
  .brand-name {
    font-size: 58px; font-weight: 800; letter-spacing: 2px; line-height: 1;
    color: var(--text-strong);
  }
  .brand-tagline {
    font-size: 23px; font-weight: 500; color: var(--text-soft); margin-top: 8px;
  }
</style>
</head>
<body>
  <div class="card">
    <div class="card-face">
      <ul class="contact-list">
        <li class="contact-item">+33610482957
          <svg class="contact-icon" viewBox="0 0 22 22" aria-hidden="true">
            <rect width="22" height="22" rx="4" fill="var(--icon-grey)"/>
            <path d="M7 5 L9 5 L10 8.5 L8.6 9.6 Q10 12.5 12.4 13.4 L13.5 12 L17 13 L17 15 Q15 17 12 15.5 Q7.5 13 6 9 Q5.5 6.5 7 5 Z" fill="var(--card-white)"/>
          </svg>
        </li>
        <li class="contact-item">xyz@mailbox-example.com
          <svg class="contact-icon" viewBox="0 0 22 22" aria-hidden="true">
            <rect width="22" height="22" rx="4" fill="var(--icon-grey)"/>
            <rect x="5" y="7" width="12" height="8.5" fill="none" stroke="var(--card-white)" stroke-width="1.6"/>
            <path d="M5 7 L11 12 L17 7" fill="none" stroke="var(--card-white)" stroke-width="1.6"/>
          </svg>
        </li>
        <li class="contact-item">www.avidatelier-example.com
          <svg class="contact-icon" viewBox="0 0 22 22" aria-hidden="true">
            <rect width="22" height="22" rx="4" fill="var(--icon-grey)"/>
            <circle cx="11" cy="11" r="6" fill="none" stroke="var(--card-white)" stroke-width="1.5"/>
            <ellipse cx="11" cy="11" rx="2.6" ry="6" fill="none" stroke="var(--card-white)" stroke-width="1.3"/>
            <line x1="5" y1="11" x2="17" y2="11" stroke="var(--card-white)" stroke-width="1.3"/>
          </svg>
        </li>
      </ul>

      <div class="person">
        <p class="person-name">Maëlle Corvadin</p>
        <p class="person-role">Président and Co-Founder</p>
      </div>

      <div class="rule rule-top"></div>
      <p class="address">27, rue Caldenois, 75005 Paris, France</p>
      <div class="rule rule-bottom"></div>

      <div class="brand">
        <p class="brand-name">LINDENFALL STUDIO</p>
        <p class="brand-tagline">The best team to provide you with high-end Furniture</p>
      </div>
    </div>
  </div>
</body>
</html>
```